Business Cards/Stationary for CIO Outsourcing Company
Velmora Solutions
Use same font as used in my logo
Dorian Halbrook
Partner
Four Maple Ridge Plaza
Suite 240
Ashcombe, Texas 77590
dhalbrook@govelmora.com
www.govelmora.com
Logo icon can be shown separate from the name if necessary on stationary.

```html
<!DOCTYPE html>
<html lang="en">
<head>
<meta charset="UTF-8">
<title>Velmora Solutions – Business Card</title>
<link href="https://fonts.googleapis.com/css2?family=Cinzel:wght@400;600&display=swap" rel="stylesheet">
<style>
  :root {
    --page-bg: #e6e4e1;
    --card-bg: #ffffff;
    --brand-red: #b3262f;
    --slate: #3f4a52;
    --ink: #3a3a3a;
    --muted: #5a5a5a;
  }
  * { margin: 0; padding: 0; box-sizing: border-box; }
  html, body {
    width: 1200px; height: 900px; overflow: hidden;
    background: var(--page-bg);
    font-family: "Cinzel", serif;
  }
  .canvas {
    width: 1200px; height: 900px;
    display: flex; align-items: center; justify-content: center;
  }
  .business-card {
    position: relative;
    width: 1000px; height: 572px;
    background: var(--card-bg);
    box-shadow: 0 6px 24px rgba(0,0,0,0.18);
    overflow: hidden;
  }
  .brand {
    position: absolute; left: 90px; top: 62px;
    display: flex; align-items: center; gap: 20px;
  }
  .brand-dot {
    width: 84px; height: 84px; border-radius: 50%;
    background: var(--brand-red);
  }
  .brand-name {
    font-size: 80px; font-weight: 400; letter-spacing: 3px;
    color: var(--brand-red); line-height: 1;
  }
  .holder {
    position: absolute; left: 300px; width: 520px; top: 262px;
    text-align: center;
  }
  .holder-name {
    font-size: 24px; color: var(--brand-red); letter-spacing: 1px;
  }
  .holder-title {
    margin-top: 4px; font-size: 20px; color: var(--ink); letter-spacing: 1px;
  }
  .contact-block {
    position: absolute; right: 40px; top: 388px;
    display: flex; flex-direction: column; align-items: flex-end; row-gap: 10px;
    font-size: 16px; color: var(--muted); letter-spacing: 0.5px;
  }
  .contact-line { display: flex; column-gap: 18px; }
  .contact-item { display: flex; align-items: center; gap: 6px; white-space: nowrap; }
  .contact-icon { width: 18px; height: 18px; flex: none; }
  .base-band {
    position: absolute; left: 0; right: 0; bottom: 0; height: 44px;
    background: var(--slate);
  }
  .web-tab {
    position: absolute; left: 360px; right: 52px; bottom: 0; height: 82px;
    background: var(--brand-red);
    border-radius: 10px 10px 0 0;
    display: flex; align-items: center; justify-content: center;
    color: #fff; font-size: 22px; letter-spacing: 7px;
  }
</style>
</head>
<body>
<main class="canvas">
  <section class="business-card">
    <div class="brand">
      <span class="brand-dot"></span>
      <span class="brand-name">VELMORA</span>
    </div>

    <div class="holder">
      <p class="holder-name">Dorian Halbrook</p>
      <p class="holder-title">Partner</p>
    </div>

    <div class="contact-block">
      <div class="contact-line">
        <span class="contact-item">
          <svg class="contact-icon" viewBox="0 0 20 20"><circle cx="10" cy="10" r="10" fill="var(--brand-red)"/><path d="M5 10.5 10 6l5 4.5v4H5z" fill="#fff"/></svg>
          Four Maple Ridge Plaza Suite 240 Ashcombe, Texas 77590
        </span>
        <span class="contact-item">
          <svg class="contact-icon" viewBox="0 0 20 20"><circle cx="10" cy="10" r="10" fill="var(--brand-red)"/><circle cx="10" cy="10" r="5" fill="none" stroke="#fff" stroke-width="1.6"/><path d="M5 10h10M10 5v10" stroke="#fff" stroke-width="1.2"/></svg>
          www.govelmora.com
        </span>
      </div>
      <div class="contact-line">
        <span class="contact-item">
          <svg class="contact-icon" viewBox="0 0 20 20"><circle cx="10" cy="10" r="10" fill="var(--brand-red)"/><path d="M6 5.5h3l1 3-1.6 1.2a7 7 0 0 0 2.9 2.9L12.5 11l3 1v3c-5 .5-10-4.5-9.5-9.5z" fill="#fff"/></svg>
          (555) 013-4827
        </span>
        <span class="contact-item">
          <svg class="contact-icon" viewBox="0 0 20 20"><circle cx="10" cy="10" r="10" fill="var(--brand-red)"/><rect x="7" y="4.5" width="6" height="11" rx="1" fill="#fff"/></svg>
          (555) 019-2265
        </span>
        <span class="contact-item">
          <svg class="contact-icon" viewBox="0 0 20 20"><circle cx="10" cy="10" r="10" fill="var(--brand-red)"/><rect x="5" y="6.5" width="10" height="7" fill="#fff"/><path d="M5 6.5l5 4 5-4" fill="none" stroke="var(--brand-red)" stroke-width="1"/></svg>
          dhalbrook@govelmora.com
        </span>
      </div>
    </div>

    <div class="base-band"></div>
    <div class="web-tab">www.govelmora.com</div>
  </section>
</main>
</body>
</html>
```